Business card design for Tolbrin Waste

I would like double-sided business cards for myself and my partner that includes our logo and the existing colour scheme. We provide waste and environmental services to customers in the motor-vehicle and engineering industries.

```html
<!DOCTYPE html>
<html lang="en">
<head>
<meta charset="utf-8">
<title>Tolbrin Waste — Business Card</title>
<link href="https://fonts.googleapis.com/css2?family=Montserrat:wght@400;500;600&family=Roboto:wght@400;500&display=swap" rel="stylesheet">
<style>
  :root {
    --backdrop: #1e1e1e;
    --card-light: #ffffff;
    --card-dark: #262626;
    --ink: #3f3f3f;
    --ink-soft: #4a4a4a;
    --green: #6aa84f;
    --green-light: #9ccc3c;
    --white: #ffffff;
  }
  * { box-sizing: border-box; margin: 0; padding: 0; }
  html, body {
    width: 1200px; height: 897px; overflow: hidden;
    background: var(--backdrop);
  }
  .canvas { position: relative; width: 1200px; height: 897px; }
  .card {
    position: absolute; left: 304px; width: 594px; height: 338px;
    border-radius: 20px; overflow: hidden;
  }
  .card-front { top: 92px; background: var(--card-light); }
  .card-back { top: 470px; background: var(--card-dark); }

  .brand-name {
    font-family: "Montserrat", sans-serif; font-weight: 600;
    text-transform: uppercase; letter-spacing: 0.02em; white-space: nowrap;
  }
  .card-front .brand-name {
    position: absolute; left: 35px; top: 38px;
    font-size: 30px; color: var(--ink-soft);
  }
  .holder-name {
    position: absolute; left: 35px; top: 114px;
    font-family: "Roboto", sans-serif; font-weight: 500;
    font-size: 24px; color: var(--green);
  }
  .holder-role {
    position: absolute; left: 35px; top: 144px;
    font-family: "Roboto", sans-serif; font-weight: 400;
    font-size: 16px; color: var(--ink);
  }
  .address {
    position: absolute; left: 35px; top: 182px;
    font-family: "Montserrat", sans-serif; font-size: 15.5px;
    line-height: 20px; color: var(--ink); font-style: normal;
  }
  .contact-list {
    position: absolute; left: 35px; top: 246px; list-style: none;
    font-family: "Montserrat", sans-serif; font-size: 15.5px; color: var(--ink);
  }
  .contact-list li { display: flex; align-items: center; height: 20.5px; }
  .contact-list svg { width: 11px; height: 11px; margin-right: 7px; flex: none; }

  .brand-ring {
    position: absolute; left: 318px; top: 64px; width: 256px; height: 256px;
  }

  .back-lockup {
    position: absolute; left: 0; top: 0; width: 100%; height: 100%;
    display: flex; align-items: center; justify-content: center; gap: 18px;
  }
  .back-lockup svg { width: 96px; height: 96px; flex: none; }
  .card-back .brand-name { font-size: 38px; color: var(--white); }
</style>
</head>
<body>
<main class="canvas">
  <section class="card card-front" aria-label="Business card front">
    <div class="brand-name">Tolbrin Waste</div>
    <h1 class="holder-name">Corin Maddox</h1>
    <p class="holder-role">Director</p>
    <address class="address">41 Wattlebrook Street<br>KELLAMBA NSW 2718</address>
    <ul class="contact-list">
      <li>
        <svg viewBox="0 0 12 12" aria-hidden="true"><path d="M3 1 L4.5 3.5 L3.6 4.6 Q4.6 7 7.4 8.4 L8.5 7.5 L11 9 L10 11 Q4 11 1 2 Z" fill="var(--green)"/></svg>
        (123) 555-0147
      </li>
      <li>
        <svg viewBox="0 0 12 12" aria-hidden="true"><rect x="1" y="2.5" width="10" height="7" fill="none" stroke="var(--green)" stroke-width="1.3"/><path d="M1 2.5 L6 6.5 L11 2.5" fill="none" stroke="var(--green)" stroke-width="1.3"/></svg>
        info@tolbrinwaste.com
      </li>
      <li>
        <svg viewBox="0 0 12 12" aria-hidden="true"><circle cx="6" cy="6" r="5" fill="none" stroke="var(--green)" stroke-width="1.2"/><ellipse cx="6" cy="6" rx="2.2" ry="5" fill="none" stroke="var(--green)" stroke-width="1"/><path d="M1 6 H11 M2 3.5 H10 M2 8.5 H10" stroke="var(--green)" stroke-width="0.9"/></svg>
        www.tolbrinwaste.com
      </li>
    </ul>
    <svg class="brand-ring" viewBox="0 0 256 256" aria-hidden="true">
      <circle cx="128" cy="128" r="121" fill="none" stroke="var(--green)" stroke-width="13"/>
    </svg>
  </section>

  <section class="card card-back" aria-label="Business card back">
    <div class="back-lockup">
      <svg viewBox="0 0 96 96" aria-hidden="true">
        <circle cx="48" cy="48" r="42" fill="none" stroke="var(--green-light)" stroke-width="6"/>
      </svg>
      <div class="brand-name">Tolbrin Waste</div>
    </div>
  </section>
</main>
</body>
</html>
```